Keystone Prime Water Tank

I primarily market the water tanks so want a business care that reflects that. I have attached the water tank logo. You have been working on our water tank so maybe we can use that on the card et. I am leaving as one sided but can be double sided if that works. The information that needs to be on the cards is as follows: Gerald T. Munro Phone numbers: Office 555-284-9137 Direct 555-619-2405 Mobile 555-372-5841 email address: gerald@fieldgearworks.com Address P.O. Box 8273 Windermere, FL 30512 Web Page: www.fieldgearworks.com. A lot to fit on the card. Thanks

```html
<!DOCTYPE html>
<html lang="en">
<head>
<meta charset="utf-8">
<title>Keystone Prime Water Tank – Business Card</title>
<link href="https://fonts.googleapis.com/css2?family=Oswald:wght@600&family=Roboto:wght@400;700&display=swap" rel="stylesheet">
<style>
  :root {
    --backdrop: #6f6f6f;
    --brand-red: #f80000;
    --brand-red-soft: #ff6b6b;
    --brand-red-pale: #ffd9d9;
    --paper-white: #ffffff;
    --card-dark: #262626;
    --ink-light: #ffffff;
  }
  html, body {
    margin: 0;
    padding: 0;
    width: 1200px;
    height: 1200px;
    overflow: hidden;
    background: var(--backdrop);
  }
  .canvas {
    position: relative;
    width: 1200px;
    height: 1200px;
  }
  .card {
    position: absolute;
    left: 257px;
    width: 686px;
    height: 392px;
    overflow: hidden;
  }
  .card--front { top: 165px; background: var(--paper-white); }
  .card--back  { top: 653px; background: var(--card-dark); }

  .front-split {
    position: absolute;
    inset: 0;
    width: 100%;
    height: 100%;
  }
  .contact-block {
    position: absolute;
    left: 33px;
    top: 161px;
    color: var(--ink-light);
    font-family: "Roboto", Arial, sans-serif;
    font-size: 16px;
    line-height: 19.3px;
  }
  .holder-name {
    margin: 0 0 19px;
    font-family: "Oswald", "Arial Narrow", sans-serif;
    font-weight: 600;
    font-size: 26px;
    line-height: 32px;
    letter-spacing: 0;
    text-transform: uppercase;
  }
  .postal-address {
    margin: 0 0 8px;
    font-style: normal;
  }
  .contact-list {
    list-style: none;
    margin: 0;
    padding: 0;
  }
  .contact-list li {
    display: flex;
    align-items: center;
    gap: 6px;
    height: 19.3px;
  }
  .contact-icon {
    width: 13px;
    height: 13px;
    flex: none;
    fill: var(--ink-light);
  }

  .brand-lockup {
    position: absolute;
    inset: 0;
    display: flex;
    align-items: center;
    justify-content: center;
    gap: 12px;
  }
  .brand-square {
    width: 22px;
    height: 22px;
    background: var(--brand-red);
  }
  .brand-name {
    margin: 0;
    color: var(--ink-light);
    font-family: "Roboto", Arial, sans-serif;
    font-weight: 700;
    font-size: 26px;
    text-transform: uppercase;
    letter-spacing: 0.5px;
  }
</style>
</head>
<body>
<main class="canvas">

  <section class="card card--front" aria-label="Card front">
    <svg class="front-split" viewBox="0 0 686 392" preserveAspectRatio="none">
      <defs>
        <linearGradient id="stripe-tone" x1="0" y1="0" x2="1" y2="1">
          <stop offset="0" stop-color="var(--brand-red-pale)"/>
          <stop offset="1" stop-color="var(--brand-red-soft)"/>
        </linearGradient>
      </defs>
      <polygon points="0,0 176,0 461,392 0,392" fill="var(--brand-red)"/>
      <polygon class="stripe-area" role="img" aria-label="Red angled stripe pattern from the tank mark"
               points="452,0 686,0 686,392 497,392 320,150"
               fill="url(#stripe-tone)"/>
    </svg>

    <div class="contact-block">
      <h1 class="holder-name">Gerald T. Munro</h1>
      <address class="postal-address">P.O. Box 8273<br>Windermere, FL 30512</address>
      <ul class="contact-list">
        <li>
          <svg class="contact-icon" viewBox="0 0 24 24" aria-label="Office"><path d="M6.6 10.8a15.1 15.1 0 0 0 6.6 6.6l2.2-2.2c.3-.3.7-.4 1-.2 1.1.4 2.3.6 3.6.6.6 0 1 .4 1 1V20c0 .6-.4 1-1 1C10.6 21 3 13.4 3 4c0-.6.4-1 1-1h3.5c.6 0 1 .4 1 1 0 1.3.2 2.5.6 3.6.1.3 0 .7-.2 1z"/></svg>
          555-284-9137
        </li>
        <li>
          <svg class="contact-icon" viewBox="0 0 24 24" aria-label="Direct"><path d="M6.6 10.8a15.1 15.1 0 0 0 6.6 6.6l2.2-2.2c.3-.3.7-.4 1-.2 1.1.4 2.3.6 3.6.6.6 0 1 .4 1 1V20c0 .6-.4 1-1 1C10.6 21 3 13.4 3 4c0-.6.4-1 1-1h3.5c.6 0 1 .4 1 1 0 1.3.2 2.5.6 3.6.1.3 0 .7-.2 1z"/></svg>
          555-619-2405
        </li>
        <li>
          <svg class="contact-icon" viewBox="0 0 24 24" aria-label="Mobile"><path d="M7 1h10a2 2 0 0 1 2 2v18a2 2 0 0 1-2 2H7a2 2 0 0 1-2-2V3a2 2 0 0 1 2-2zm0 3v15h10V4z"/></svg>
          555-372-5841
        </li>
        <li>
          <svg class="contact-icon" viewBox="0 0 24 24" aria-label="Email"><path d="M2 5h20v14H2zm2 2v.4l8 5 8-5V7l-8 5z"/></svg>
          gerald@fieldgearworks.com
        </li>
        <li>
          <svg class="contact-icon" viewBox="0 0 24 24" aria-label="Website"><path d="M12 2a10 10 0 1 0 0 20 10 10 0 0 0 0-20zm-1 17.9A8 8 0 0 1 4.2 10L9 14.8v1a2 2 0 0 0 2 2zm6.9-2.5a2 2 0 0 0-1.9-1.4h-1v-3a1 1 0 0 0-1-1H8v-2h2a1 1 0 0 0 1-1V7h2a2 2 0 0 0 2-2v-.4a8 8 0 0 1 2.9 12.8z"/></svg>
          www.fieldgearworks.com
        </li>
      </ul>
    </div>
  </section>

  <section class="card card--back" aria-label="Card back">
    <div class="brand-lockup">
      <span class="brand-square" aria-hidden="true"></span>
      <p class="brand-name">Keystone Prime Water Tank</p>
    </div>
  </section>

</main>
</body>
</html>
```